Business Card for Kinesiologist Practitioner

I need a logo and business card designing for a Kinesiologist Practitioner. I would like the card to be double sided. The look and feel of the logo and graphics should depict natural healing and well being. I would like a modern, fresh and contemporary design with a professional style. I have attached some logos and business cards that I liek from other natural health practitioners. I have also attached some logos that I like and a mock up of the business card style. Please however use your own creative input to change any element as you feel appropriate.

I have used the strap line "Quiet Renewal" which I would like underneath the logo. For the logo I like natural objects and possibly with 3 elements in the design as the course I have studied follows a "Open Arc " healing concept (mind, body, soul). Maybe a tree or flower with 3 elements and a representation or suggestion of the human body somehow. You will see from the logos i have uploaded

Industry/Entity Type

Business

Contact Information for Business Card

Please see the mock up attached.

Font styles to use
Serif
Sans Serif

Colors
faa54b
acd036
fbee3d
85cae6

Requirements
Must have
• Note the colours are just suggested colours. Please us your own creative licence.

```html
<!DOCTYPE html>
<html lang="en">
<head>
<meta charset="utf-8">
<title>Quiet Renewal — Business Card</title>
<link rel="stylesheet" href="https://fonts.googleapis.com/css2?family=Raleway:wght@400;500;800&display=swap">
<style>
  :root {
    --bg: #e6e6e3;
    --card: #ffffff;
    --ink: #1f1f1f;
    --leaf: #8cc63f;
    --shadow: rgba(0, 0, 0, 0.18);
  }
  * { margin: 0; padding: 0; box-sizing: border-box; }
  html, body {
    width: 1200px; height: 900px; overflow: hidden;
    background: var(--bg);
    font-family: "Raleway", sans-serif;
    color: var(--ink);
  }
  .canvas {
    position: relative; width: 1200px; height: 900px;
  }
  .card {
    position: absolute; left: 250px;
    width: 700px; height: 390px;
    background: var(--card);
    box-shadow: 0 6px 18px var(--shadow);
  }
  .card--front { top: 50px; }
  .card--back { top: 465px; }

  /* Front */
  .front-brand {
    position: absolute; left: 0; right: 0; top: 110px;
    display: flex; flex-direction: column; align-items: center;
  }
  .brand-dot {
    width: 70px; height: 70px; border-radius: 50%;
    background: var(--leaf); margin-bottom: 34px;
  }
  .brand-name {
    font-weight: 400; font-size: 30px; letter-spacing: 0.32em;
    padding-left: 0.32em; text-transform: uppercase; color: var(--ink);
  }
  .tagline {
    margin-top: 18px; font-size: 19px; font-weight: 500; letter-spacing: 0.02em;
  }
  .tagline .sep { color: var(--leaf); margin: 0 6px; }

  /* Back */
  .person {
    position: absolute; right: 50px; top: 36px; text-align: right;
  }
  .person__name { font-size: 27px; font-weight: 800; letter-spacing: 0.01em; }
  .person__cred { font-weight: 400; }
  .person__role {
    margin-top: 2px; font-size: 17px; font-weight: 400;
    letter-spacing: 0.3em; color: var(--leaf);
  }
  .back-brand {
    position: absolute; left: 60px; top: 150px;
    display: flex; flex-direction: column; align-items: center;
  }
  .back-brand .brand-dot { width: 56px; height: 56px; margin-bottom: 26px; }
  .back-brand .brand-name { font-size: 20px; letter-spacing: 0.26em; }
  .contact {
    position: absolute; right: 45px; bottom: 40px;
    list-style: none; text-align: right;
  }
  .contact__item {
    display: flex; align-items: center; justify-content: flex-end;
    gap: 12px; font-size: 25px; line-height: 1.5;
  }
  .contact__icon { width: 24px; height: 24px; flex: none; }
</style>
</head>
<body>
<main class="canvas">

  <section class="card card--front" aria-label="Card front">
    <div class="front-brand">
      <span class="brand-dot" aria-hidden="true"></span>
      <p class="brand-name">Quiet Renewal</p>
      <p class="tagline">mind<span class="sep">|</span>body<span class="sep">|</span>soul</p>
    </div>
  </section>

  <section class="card card--back" aria-label="Card back">
    <div class="person">
      <p class="person__name">CLARA VENNICK <span class="person__cred">dip. cert.</span></p>
      <p class="person__role">KINESIOLOGIST</p>
    </div>

    <div class="back-brand">
      <span class="brand-dot" aria-hidden="true"></span>
      <p class="brand-name">Quiet Renewal</p>
    </div>

    <ul class="contact">
      <li class="contact__item">0400 217 395
        <svg class="contact__icon" viewBox="0 0 24 24" aria-hidden="true">
          <circle cx="12" cy="12" r="10.5" fill="none" stroke="var(--leaf)" stroke-width="1.8"/>
          <path d="M8.3 6.8c.5-.4 1.1-.3 1.4.2l1 1.7c.3.5.1 1-.3 1.3l-.6.4c.5 1.3 1.5 2.4 2.8 3l.5-.6c.3-.4.9-.5 1.3-.2l1.6 1.1c.5.3.5 1 .1 1.4l-.7.7c-.6.6-1.6.7-2.4.3-2.6-1.3-4.6-3.4-5.7-6-.3-.8-.1-1.8.5-2.4z" fill="var(--leaf)"/>
        </svg>
      </li>
      <li class="contact__item">claravennick@mailbox.com
        <svg class="contact__icon" viewBox="0 0 24 24" aria-hidden="true">
          <rect x="2" y="5" width="20" height="14" fill="none" stroke="var(--leaf)" stroke-width="1.8"/>
          <path d="M2 5l10 8 10-8M2 19l7.5-7M22 19l-7.5-7" fill="none" stroke="var(--leaf)" stroke-width="1.6"/>
        </svg>
      </li>
    </ul>
  </section>

</main>
</body>
</html>
```